Bright Current Electrical & Communications business card design

We would like a double sided business card that is different. Want it to be exciting and fun. Something that people keep rather then just throw it in the bin.
We have a logo that we want to put on one side of the business card and then the business information on the reverse side. Trying to go for a real professional style of business card

Target Market(s)

Electrical

Industry/Entity Type

Electrical

Contact Information for Business Card

Bright Current Electrical & Communications
Glen Ashworth
P: 0437 862 305
E: brightcurrent@mailbox-example.com.au
Lic No: 574106K
24/7

Font styles to use
Other font styles liked:
• Would like ideas

Requirements
Must have
• Our company logo (preferably on both sides) yellow needs to be incorporated somewhere. Business card card colours to match with logo. Maybe a small pop of colour
Nice to have
• Open to some design ideas

```html
<!DOCTYPE html>
<html lang="en">
<head>
<meta charset="utf-8">
<title>Bright Current Electrical &amp; Communications – Business Card</title>
<link rel="stylesheet" href="https://fonts.googleapis.com/css2?family=Michroma&family=Nunito:wght@900&family=Open+Sans:wght@400;700&display=swap">
<style>
  :root {
    --backdrop: #e9eaeb;
    --card-cream: #fefef2;
    --card-blue: #00b4eb;
    --brand-yellow: #fff200;
    --brand-grey: #6d6e70;
    --white: #ffffff;
    --shadow: rgba(0, 0, 0, 0.18);
  }
  * { margin: 0; padding: 0; box-sizing: border-box; }
  html, body {
    width: 1200px;
    height: 899px;
    overflow: hidden;
    background: var(--backdrop);
  }
  .canvas {
    position: relative;
    width: 1200px;
    height: 899px;
  }
  .card {
    position: absolute;
    left: 350px;
    width: 501px;
    height: 278px;
    box-shadow: 3px 4px 6px var(--shadow);
  }
  .card--front {
    top: 127px;
    background: var(--card-cream);
    border-radius: 0 56px 0 56px;
  }
  .card--back {
    top: 453px;
    background: var(--card-blue);
    border-radius: 56px 0 56px 0;
  }
  .wordmark {
    position: absolute;
    left: 0;
    right: 0;
    top: 118px;
    text-align: center;
    font-family: "Michroma", sans-serif;
    font-weight: 400;
    font-size: 15px;
    line-height: 26px;
    letter-spacing: 0.5px;
    color: var(--brand-grey);
    text-transform: uppercase;
  }
  .holder-name {
    position: absolute;
    right: 291px;
    top: 70px;
    text-align: right;
    font-family: "Nunito", sans-serif;
    font-weight: 900;
    font-size: 35px;
    line-height: 38px;
    letter-spacing: -1px;
    color: var(--brand-yellow);
  }
  .contact-list {
    position: absolute;
    left: 233px;
    top: 77px;
    list-style: none;
    font-family: "Open Sans", sans-serif;
    font-size: 12.5px;
    line-height: 24.5px;
    color: var(--white);
    white-space: nowrap;
  }
  .contact-list b { font-weight: 700; }
  .divider {
    position: absolute;
    left: 43px;
    top: 200px;
    width: 415px;
    height: 3px;
    background: var(--white);
  }
  .company-line {
    position: absolute;
    left: 43px;
    width: 415px;
    top: 216px;
    text-align: center;
    font-family: "Michroma", sans-serif;
    font-size: 10.3px;
    letter-spacing: 0.6px;
    color: var(--white);
    text-transform: uppercase;
    white-space: nowrap;
  }
</style>
</head>
<body>
  <main class="canvas">
    <section class="card card--front" aria-label="Card front">
      <p class="wordmark">Bright Current<br>Electrical &amp; Communications</p>
    </section>

    <section class="card card--back" aria-label="Card back">
      <h1 class="holder-name">Glen<br>Ashworth</h1>
      <ul class="contact-list">
        <li><b>P:</b> 0437 862 305</li>
        <li><b>E:</b> brightcurrent@mailbox-example.com.au</li>
        <li>License No: 574106K &nbsp;|&nbsp; 24/7</li>
      </ul>
      <div class="divider"></div>
      <p class="company-line">Bright Current Electrical &amp; Communications</p>
    </section>
  </main>
</body>
</html>
```